Tranquil Harbour Hypnotherapy 2017 DL Card Flyer

We would like a double sided DL Card Flyer design.

We are a professional Hypnotherapy Clinic looking for a fresh clean design.

Front of card is summary info and back of flyer is detailed text.

I have attached documents with text for the front (dl size hypno 1) and back (dl size hypno 2) of the card and an indicative style of layout.

There are logo files uploaded as well as one image file.

The colors we like are blue, white and yellow/gold.
Updates

please note: when using the 'new mindset new results' image, please only use the top half of the image. The girl is not to be in the image, just the words and light bulb with the chalk underline. thanks.. Added Sunday, March 19, 2017

Industry/Entity Type

Health And Wellness

Requirements
Must have
• Note. I have misspelled the www.TranquilHarbourHypnotherapy.com.au (missing an 'o' in the attachments to the brief). My error. Please amend in your design submissions.

```html
<!DOCTYPE html>
<html lang="en">
<head>
<meta charset="utf-8">
<title>Tranquil Harbour Hypnotherapy DL Flyer</title>
<link href="https://fonts.googleapis.com/css2?family=Open+Sans:wght@400;600;700;800&family=Roboto+Condensed:wght@400;700&display=swap" rel="stylesheet">
<style>
  :root {
    --navy: #1f2c6e;
    --navy-bright: #2a3a8f;
    --ink: #1d1d1d;
    --rule: #8a8a8a;
    --paper: #fbfbfb;
    --page: #e6e6e6;
    --charcoal: #2b2b2b;
  }
  * { box-sizing: border-box; margin: 0; padding: 0; }
  html, body { width: 1200px; height: 1200px; overflow: hidden; }
  body { background: var(--page); position: relative; font-family: "Roboto Condensed", sans-serif; color: var(--ink); }

  .card { position: absolute; top: 39px; width: 546px; height: 1122px; background: var(--paper); box-shadow: 0 2px 6px rgba(0,0,0,.25); overflow: hidden; }
  .card--front { left: 37px; }
  .card--back { left: 618px; }
  .abs { position: absolute; }

  /* front */
  .brand-dot { left: 93px; top: 38px; width: 116px; height: 116px; border-radius: 50%; background: var(--navy); }
  .brand-divider { left: 217px; top: 42px; width: 2px; height: 106px; background: var(--rule); }
  .brand-name { left: 233px; top: 64px; font-family: "Open Sans", sans-serif; font-weight: 700; font-size: 25px; line-height: 1.15; color: var(--navy); }
  .chevron { left: 0; top: 168px; }
  .frame-side { width: 1px; background: var(--rule); }
  .headline { left: 0; width: 546px; top: 250px; text-align: center; font-family: "Open Sans", sans-serif; color: var(--navy); }
  .headline__lead { font-size: 57px; font-weight: 400; line-height: 1.05; letter-spacing: -0.5px; }
  .headline__mid { font-size: 40px; font-weight: 700; color: #222; line-height: 1.15; letter-spacing: -0.3px; }
  .headline__key { font-size: 56px; font-weight: 800; line-height: 1.05; }
  .chalk-panel { left: 0; top: 460px; width: 546px; height: 202px; background: radial-gradient(circle at 50% 50%, #7a7550 0%, #3d3d39 30%, #2c2c2c 100%); }
  .programs-title { left: 0; width: 546px; top: 720px; text-align: center; font-weight: 700; font-size: 27px; color: var(--navy); }
  .prog { width: 190px; text-align: center; font-size: 20px; line-height: 23px; color: #222; }
  .prog__icon { display: block; margin: 0 auto 8px; width: 42px; height: 42px; border-radius: 50%; background: var(--navy); }
  .footer-band { left: 0; top: 995px; }
  .footer-phone { left: 0; width: 546px; top: 1057px; text-align: center; color: #fff; font-weight: 700; font-size: 21px; }
  .footer-phone svg { vertical-align: -3px; margin-right: 8px; }
  .footer-url { left: 0; width: 546px; top: 1087px; text-align: center; color: #fff; font-size: 16px; }

  /* back */
  .back-frame { left: 20px; top: 19px; width: 507px; height: 1030px; border: 1px solid var(--rule); }
  .section-band { left: 0; width: 546px; height: 33px; background: var(--navy); color: #fff; font-weight: 700; font-size: 17.5px; text-align: center; line-height: 33px; }
  .section-icon { width: 62px; height: 62px; margin-left: -31px; left: 273px; border-radius: 50%; background: var(--navy); }
  .section-text { left: 40px; width: 466px; font-size: 16px; line-height: 19.7px; text-align: justify; text-align-last: center; }
  .section-text strong { font-weight: 700; }
  .closing-bar { left: 0; top: 1048px; width: 546px; height: 55px; background: var(--charcoal); color: #f2f2f2; font-size: 16px; line-height: 19.7px; padding: 8px 40px 0; text-align: justify; text-align-last: center; }
  .closing-rule { left: 0; top: 1106px; width: 546px; height: 2px; background: var(--navy-bright); }
</style>
</head>
<body>

<section class="card card--front">
  <div class="abs brand-dot"></div>
  <div class="abs brand-divider"></div>
  <div class="abs brand-name">Tranquil Harbour<br>Hypnotherapy</div>

  <svg class="abs chevron" width="546" height="50" viewBox="0 0 546 50">
    <polyline points="0,36 273,7 546,36" fill="none" stroke="#1f2c6e" stroke-width="5"/>
  </svg>

  <div class="abs frame-side" style="left:19px;top:210px;height:250px"></div>
  <div class="abs frame-side" style="left:526px;top:210px;height:250px"></div>

  <div class="abs headline">
    <div class="headline__lead">There is nothing</div>
    <div class="headline__mid">more important than</div>
    <div class="headline__key">GOOD HEALTH</div>
  </div>

  <div class="abs chalk-panel" role="img" aria-label="Chalkboard showing 'New Mindset, New Results' with a glowing light bulb and chalk underline"></div>

  <div class="abs frame-side" style="left:19px;top:662px;height:340px"></div>
  <div class="abs frame-side" style="left:526px;top:662px;height:340px"></div>

  <h2 class="abs programs-title">Professional Hypnosis Therapy Programs:</h2>

  <div class="abs prog" style="left:14px;top:788px"><span class="prog__icon"></span>Weight Loss<br>(Virtual Gastric Band)</div>
  <div class="abs prog" style="left:177px;top:788px"><span class="prog__icon"></span>Stress Relief &amp;<br>Deep Relaxation</div>
  <div class="abs prog" style="left:349px;top:788px"><span class="prog__icon"></span>Chronic Fatigue &amp;<br>Chronic Pain Relief</div>
  <div class="abs prog" style="left:99px;top:916px"><span class="prog__icon"></span>Sugar Addiction</div>
  <div class="abs prog" style="left:265px;top:916px"><span class="prog__icon"></span>Quit Smoking</div>

  <svg class="abs footer-band" width="546" height="127" viewBox="0 0 546 127">
    <polygon points="0,12 273,30 546,0 546,127 0,127" fill="#2a3a8f"/>
    <polygon points="0,12 273,30 546,10 546,127 0,127" fill="#1f2c6e"/>
  </svg>
  <div class="abs footer-phone">
    <svg width="24" height="18" viewBox="0 0 24 18"><path d="M2 6c0-3 4-5 10-5s10 2 10 5l-4 1-1-3H7L6 7 2 6zM7 8h10l3 9H4z" fill="#fff"/><circle cx="12" cy="12" r="2.5" fill="#1f2c6e"/></svg>1300 555 014
  </div>
  <div class="abs footer-url">www.TranquilHarbourHypnotherapy.com.au</div>
</section>

<section class="card card--back">
  <div class="abs back-frame"></div>

  <div class="abs section-icon" style="top:23px"></div>
  <h3 class="abs section-band" style="top:71px">WEIGHT LOSS PROGRAM (Virtual Gastric Band)</h3>
  <p class="abs section-text" style="top:114px">Achieve long term weight loss without dieting. Whether it’s losing 3kg or 30kg, we’ll help you become the shape and size you want to be. Our Internationally Accredited Program is proven to be 95% effective in clinical trials. Number of Sessions: 6+</p>

  <div class="abs section-icon" style="top:207px"></div>
  <h3 class="abs section-band" style="top:252px">SUGAR ADDICTION PROGRAM</h3>
  <p class="abs section-text" style="top:298px">Excess sugar intake can lead to obesity, Type 2 Diabetes and tooth decay. The habit of reaching for soft drinks, chocolate, sweets, cakes and biscuits can be hard to break.By rewiring your subconscious habits, our Program puts you back in control.<br>Number of Sessions: 3+</p>

  <div class="abs section-icon" style="top:410px"></div>
  <h3 class="abs section-band" style="top:458px">QUIT SMOKING PROGRAM</h3>
  <p class="abs section-text" style="top:503px">The facts speak for themselves. You are 10 times more likely to quit smoking for good using hypnotherapy. Expect to be a non smoker after completing the first session of our Program. (12 Month Guarantee)<br>Number of Sessions: 2</p>

  <div class="abs section-icon" style="top:597px"></div>
  <h3 class="abs section-band" style="top:647px">CHRONIC FATIGUE &amp; CHRONIC PAIN RELIEF PROGRAM</h3>
  <p class="abs section-text" style="top:696px">Chronic Fatigue, Fibromyalgia and Chronic Musculoskeletal Pain are diseases of modern living. The <strong>symptoms</strong> of fatigue and pain are very real, however the <strong>cause</strong> is usually emotional, and is generally hidden beyond our conscious awareness. Our Program comprises Education and Hypnosis to help you regain your health, your self esteem, your friends and your life, all in a manageable timeframe.<br>Number of Sessions: 6+</p>

  <div class="abs section-icon" style="top:850px"></div>
  <h3 class="abs section-band" style="top:897px">STRESS RELIEF &amp; DEEP RELAXATION PROGRAM</h3>
  <p class="abs section-text" style="top:947px">Our Program gently uncovers the true source of your stress, and helps you reconnect to a natural inner calm. We teach you self hypnosis so that you have the tools to continue your experience.<br>Number of Sessions: 3+</p>

  <p class="abs closing-bar">All Programs include take home CD’s personally recorded by our therapists, using advanced hypnotic techniques.</p>
  <div class="abs closing-rule"></div>
</section>

</body>
</html>
```